Design einer Preisliste
Zielgruppe
Wir produzieren und verkaufen Suppen Konserven und Konzentrate an Gewerbetreibende + Endabnehmer.
Wir sind im Premium Segment angesiedelt.
Hauptsächlicher Vertrieb erfolgt über den Großhandel
Die Firma ist über 80 Jahre alt
https://www.morvak-eintopf.de/
Aufgabenstellung
Unsere Preisliste soll neu designed werden.
Vorgaben sind:
Hochwertig + Elegant
Eher konservativ gehalten als zu bunt.
Die neuen Preise müssen in die Liste mit eingepflegt werden
Die alte Preisliste und die neuen Preise werden mit beigefügt.

```html
<!DOCTYPE html>
<html lang="de">
<head>
<meta charset="utf-8">
<title>Morvak Foodservice – Preisliste</title>
<link href="https://fonts.googleapis.com/css2?family=Great+Vibes&family=PT+Serif&family=Roboto+Condensed:wght@300;400;700&display=swap" rel="stylesheet">
<style>
:root{
  --bg:#ebebeb;
  --paper:#ffffff;
  --gold:#c49a1c;
  --ink:#2a2a2a;
  --muted:#555;
  --rule:#d8d8d8;
}
*{box-sizing:border-box;margin:0;padding:0}
html,body{width:1200px;height:756px;overflow:hidden;background:var(--bg)}
body{position:relative;font-family:"Roboto Condensed",sans-serif;color:var(--ink)}
.page{position:absolute;background:var(--paper);overflow:hidden;border:1px solid #d0d0d0}
.abs{position:absolute}
.brand{position:absolute;font-family:"Roboto Condensed",sans-serif;font-weight:700;color:var(--gold);font-size:15px;letter-spacing:.5px;text-align:center;width:80px;line-height:1}
.brand small{display:block;font-size:4px;font-weight:700;letter-spacing:.6px;margin-top:1px}
.banner{position:absolute;color:#fff;font-family:"PT Serif",serif;text-align:right;line-height:1.05;padding:3px 5px;display:flex;align-items:flex-end;justify-content:flex-end}
.banner span{font-size:11px}
.sub{position:absolute;font-size:4px;color:var(--ink)}
table.pl{position:absolute;border-collapse:collapse;font-size:2.3px;line-height:1.35;color:var(--ink)}
table.pl th{font-weight:700;text-align:left;padding-bottom:2px;vertical-align:bottom}
table.pl td{padding:1.2px 0;vertical-align:top}
table.pl td.n{font-weight:700;width:34%}
table.pl td.n small{display:block;font-weight:300;font-size:2px}
.copy{position:absolute;font-size:3.4px;line-height:1.42;text-align:justify;font-weight:300}
.photo{position:absolute}
</style>
</head>
<body>

<!-- Titelseite -->
<section class="page" style="left:39px;top:64px;width:210px;height:298px">
  <div class="photo" role="img" aria-label="Foto einer hellen Cremesuppe mit Spinatblättern und Croûtons im Teller" style="inset:0;background:radial-gradient(ellipse at 70% 70%,#d9cfa8 0%,#ece6cf 45%,#f6f4ee 75%,#e2e2e2 100%)"></div>
  <div class="brand" style="left:65px;top:16px">Morvak<small>Foodservice</small></div>
  <div class="abs" style="left:72px;top:58px;font-size:5px;letter-spacing:.4px;color:#333">FÜR DIE &nbsp;&nbsp;&nbsp;&nbsp;&nbsp;&nbsp; GEHOBENE</div>
  <div class="abs" style="left:26px;top:60px;font-family:'Great Vibes',cursive;font-size:46px;color:#1d1d1d;line-height:1">Gastronomie</div>
  <div class="abs" style="left:0;width:210px;top:265px;text-align:center;font-size:5px;letter-spacing:.3px;color:#444">GROSSVERBRAUCHER-SORTIMENTSLISTE</div>
</section>

<!-- Doppelseite 1 -->
<section class="page" style="left:281px;top:64px;width:423px;height:300px">
  <div class="brand" style="left:65px;top:16px">Morvak<small>Foodservice</small></div>
  <p class="copy" style="left:19px;top:48px;width:85px">Morvak steht für vorbildliche und gepflegte Gastlichkeit in der gehobenen Gastronomie, im guten GV-Service und im Top-Party-Service. Genial und edler als Trockenprodukte. Sie können mit Morvak Spezialitäten allen Ansprüchen Ihrer Gäste nach einer kleinen Mahlzeit gerecht werden. Schneller, besser und wirtschaftlicher geht es nicht! Wir garantieren qualitative Beständigkeit und Unverfälschtheit. Das sieht man und das schmeckt man!<br><br>Unser Motto: Mit den richtigen Produkten gewinnen! Spitzenqualität und appetitliches Aussehen sind die Hauptanforderung der Tischgäste. Aber das alleine reicht heute nicht mehr aus. Unsere Verwender fordern darüber hinaus convience – gestützte Spezialitäten und diese möglichst deklarationsfrei. Das sind für unsere Kunden wichtige Kriterien beim Einkauf.</p>
  <p class="copy" style="left:108px;top:48px;width:85px">Wir bieten deshalb zukünftig überwiegend deklarationsfreie Artikel an. Das sagt der Gesetzgeber: Zusatzstoffe müssen auf den Speisekarten besonders gekennzeichnet werden. Es geht hier um Zusätze mit technologischer Wirkung.<br><br>Die Güte der Endprodukte wird durch die Verwendung nur bester Rohstoffe gewährleistet. Wir vertreiben unsere Topqualität unter dem Motto "First Class". Seit mehr als 80 Jahren liefern wir immer pünktlich ohne Qualitätsreklamationen. Die Auslieferung erfolgt nach Auftragseingang am folgenden Tag.<br><br>Die Rückverfolgung der einzelnen Produktionschargen ist sichergestellt. Alle Morvak Produkte haben eine garantierte Restlaufzeit von mindestens 30 Monaten.</p>
  <div class="photo" role="img" aria-label="Foto einer weißen Spargelcremesuppe in einer Schale mit Petersilie auf karierter Serviette" style="left:19px;top:150px;width:174px;height:135px;background:linear-gradient(160deg,#cfd6dd 0%,#f3f2ee 40%,#e9e5da 70%,#b9c6d6 100%)"></div>

  <div class="banner" role="img" aria-label="Foto konzentrierter Saucen mit Gemüse" style="left:231px;top:13px;width:173px;height:30px;background:linear-gradient(90deg,#7a2e14,#b4532a 50%,#8d3a1c)"><span>Konzentrierten Saucen</span></div>
  <div class="sub" style="left:231px;top:45px">Gebündelte Kompetenz im Marktsegment ★★★★ Gastronomie</div>
  <table class="pl" style="left:231px;top:52px;width:173px">
    <tr><th></th><th>Nr.</th><th>Gebinde</th><th>Inhalt</th><th>Euro</th><th>Ergiebig.</th><th>Karton</th><th>EAN</th><th>Preis</th></tr>
    <tr><td class="n">Hühnersuppe<small>mit Fleischeinlage, konzentriert</small></td><td>001</td><td>1/4 Dose</td><td>212 ml</td><td>1,40</td><td>0,45 l</td><td>50x1</td><td>001045</td><td>100,00</td></tr>
    <tr><td class="n">Gebundene Ochsenschwanz EXTRA<small>mit extra viel Fleischeinlage</small></td><td>007</td><td>1/1 Dose</td><td>850 ml</td><td>5,25</td><td>1,80 l</td><td>12x1</td><td>003342</td><td>80,00</td></tr>
    <tr><td class="n">Ungarische Gulaschsuppe ROYAL<small>mit doppelter Fleischeinlage</small></td><td>018</td><td>1/4 Dose</td><td>212 ml</td><td>1,85</td><td>0,45 l</td><td>50x1</td><td>003483</td><td>92,50</td></tr>
    <tr><td class="n">Ungarische Gulaschsuppe EXTRA<small>mit extra viel Fleischeinlage</small></td><td>014</td><td>1/1 Dose</td><td>850 ml</td><td>5,35</td><td>1,80 l</td><td>12x1</td><td>003349</td><td>80,00</td></tr>
    <tr><td class="n">Ungarische Gulaschsuppe I<small>mit reichlicher Fleischeinlage</small></td><td>218</td><td>5/1 Dose</td><td>4250 ml</td><td>20,75</td><td>9,00 l</td><td>2x1</td><td>000375</td><td>41,50</td></tr>
    <tr><td class="n">Klare Rindfleischsuppe<small>mit großer Fleischeinlage</small></td><td>021</td><td>1/4 Dose</td><td>212 ml</td><td>3,40</td><td>1,50 l</td><td>50x1</td><td>004044</td><td>180,00</td></tr>
  </table>
  <div class="banner" role="img" aria-label="Foto klassischer Suppen in dunklen Rottönen" style="left:231px;top:149px;width:173px;height:30px;background:linear-gradient(90deg,#5e1d0e,#9a3b1c 60%,#c15a2c)"><span>Klassische Spezialitäten<br>tafelfertig</span></div>
  <div class="sub" style="left:231px;top:181px">Etwas Attraktives in Top-Qualität auf den Tisch bringen</div>
  <table class="pl" style="left:231px;top:188px;width:173px">
    <tr><th></th><th>Nr.</th><th>Gebinde</th><th>Inhalt</th><th>Euro</th><th>Ergiebig.</th><th>Karton</th><th>EAN</th><th>Preis</th></tr>
    <tr><td class="n">Klare Ochsenschwanz ROYAL<small>eine international geschätzte Kraftsuppe</small></td><td>040</td><td>1/4 Ringpull</td><td>212 ml</td><td>1,90</td><td>1 Port.</td><td>50x1</td><td>001224</td><td>95,00</td></tr>
    <tr><td class="n">Französische Zwiebelsuppe<small>gebunden, aus frischen Zwiebeln</small></td><td>046</td><td>1/4 Ringpull</td><td>212 ml</td><td>1,40</td><td>1 Port.</td><td>50x1</td><td>000734</td><td>70,00</td></tr>
    <tr><td class="n">Tomaten Creme<small>toskanisch, ohne Einlage</small></td><td>116</td><td>1/4 Ringpull</td><td>212 ml</td><td>1,40</td><td>1 Port.</td><td>50x1</td><td>001830</td><td>70,00</td></tr>
    <tr><td class="n">Kessel-Gulasch-Suppe<small>mit reichlicher Einlage</small></td><td>097</td><td>1/4 Ringpull</td><td>212 ml</td><td>1,40</td><td>1 Port.</td><td>50x1</td><td>004750</td><td>70,00</td></tr>
  </table>
</section>

<!-- Doppelseite 2 -->
<section class="page" style="left:729px;top:67px;width:421px;height:299px">
  <div class="brand" style="left:65px;top:16px">Morvak<small>Foodservice</small></div>
  <div class="banner" role="img" aria-label="Foto einer gelben Suppe mit frischen Kräutern" style="left:19px;top:44px;width:173px;height:30px;background:linear-gradient(90deg,#e2b64a,#d99a1e 50%,#c27a12)"><span>Perfekt – schnell + einfach</span></div>
  <div class="sub" style="left:19px;top:76px">Dem Koch bleibt der volle Spielraum für seine persönliche Note</div>
  <table class="pl" style="left:19px;top:83px;width:173px">
    <tr><th></th><th>Nr.</th><th>Gebinde</th><th>Inhalt</th><th>Euro</th><th>Ergiebig.</th><th>Karton</th><th>EAN</th><th>Preis</th></tr>
    <tr><td class="n">Hühnersuppe 1:10<small>ohne Fleisch, 8 l Suppenbasis</small></td><td>004</td><td>1/1 Dose</td><td>850 ml</td><td>7,05</td><td>8,00 l</td><td>12x1</td><td>00022</td><td>84,60</td></tr>
    <tr><td class="n">Rindsuppe 1:10<small>ohne Fleisch, 8 l Suppenbasis</small></td><td>005</td><td>1/1 Dose</td><td>850 ml</td><td>7,05</td><td>8,00 l</td><td>12x1</td><td>00543</td><td>84,60</td></tr>
    <tr><td class="n">Klare Gemüsesuppe 1:10<small>8 l Suppenbasis, rein vegetarisch</small></td><td>152</td><td>1/1 Dose</td><td>850 ml</td><td>7,05</td><td>8,00 l</td><td>12x1</td><td>00895</td><td>84,60</td></tr>
    <tr><td class="n">Klare Fischsuppe 1:5<small>4 l Suppenbasis oder 2 l Saucenfond</small></td><td>207</td><td>1/1 Dose</td><td>850 ml</td><td>7,05</td><td>8,00 l</td><td>12x1</td><td>003240</td><td>84,60</td></tr>
    <tr><td class="n">Wild-Kraft-Fond 1:5<small>4 l Suppenbasis oder 2 l Saucenfond</small></td><td>210</td><td>1/1 Dose</td><td>850 ml</td><td>7,05</td><td>8,00 l</td><td>12x1</td><td>003503</td><td>84,60</td></tr>
    <tr><td class="n">Kalbs-Kraft-Fond<small>4 l Suppenbasis oder 2 l Saucenfond</small></td><td>141</td><td>1/1 Dose</td><td>850 ml</td><td>6,95</td><td>8,00 l</td><td>12x1</td><td>001240</td><td>83,90</td></tr>
    <tr><td class="n">Braten-Kraft-Fond 1:10<small>8 l Suppenbasis oder 5 l Saucenfond</small></td><td>148</td><td>1/1 Dose</td><td>850 ml</td><td>7,05</td><td>8,00 l</td><td>12x1</td><td>001105</td><td>84,60</td></tr>
    <tr><td class="n">Rindfleischsuppe 1:12<small>ohne Fett, ohne Fleisch, 10 l Suppenbasis</small></td><td>027</td><td>1/1 Dose</td><td>850 ml</td><td>7,05</td><td>8,00 l</td><td>12x1</td><td>00116</td><td>84,60</td></tr>
    <tr><td class="n">Hühnersuppe 1:12<small>ohne Fett, ohne Fleisch, 10 l Suppenbasis</small></td><td>005</td><td>1/1 Dose</td><td>850 ml</td><td>7,05</td><td>8,00 l</td><td>12x1</td><td>00574</td><td>84,60</td></tr>
  </table>
  <div class="banner" role="img" aria-label="Foto einer Seafood-Suppe mit Kräutern" style="left:19px;top:196px;width:173px;height:30px;background:linear-gradient(90deg,#efe6d6,#e7c9a6 50%,#d9a77a)"><span>Seafood Spezialitäten<br>tafelfertig</span></div>
  <div class="sub" style="left:19px;top:228px">Für das à la carte Geschäft im Hochpreissegment</div>
  <table class="pl" style="left:19px;top:235px;width:173px">
    <tr><th></th><th>Nr.</th><th>Gebinde</th><th>Inhalt</th><th>Euro</th><th>Ergiebig.</th><th>Karton</th><th>EAN</th><th>Preis</th></tr>
    <tr><td class="n">Norwegische Lachscreme<small>aus Wildlachsfilet</small></td><td>200</td><td>1/4 Ringpull</td><td>212 ml</td><td>1,80</td><td>1 Port.</td><td>50x1</td><td>003405</td><td>90,00</td></tr>
    <tr><td class="n">Feine Hummersuppe<small>mit einem Schuss Weinbrand</small></td><td>194</td><td>1/4 Ringpull</td><td>212 ml</td><td>1,80</td><td>1 Port.</td><td>50x1</td><td>002506</td><td>90,00</td></tr>
    <tr><td class="n">Küsten-Krabbensuppe<small>mit 25g Tiefseekrabben</small></td><td>192</td><td>1/4 Ringpull</td><td>212 ml</td><td>1,90</td><td>1 Port.</td><td>50x1</td><td>002704</td><td>95,00</td></tr>
    <tr><td class="n">Küsten-Krabbensuppe<small>mit 25g Nordseekrabben</small></td><td>195</td><td>1/4 Ringpull</td><td>212 ml</td><td>2,05</td><td>1 Port.</td><td>50x1</td><td>002902</td><td>102,50</td></tr>
  </table>

  <div class="banner" role="img" aria-label="Foto einer hellen vegetarischen Cremesuppe mit Kräutern" style="left:230px;top:13px;width:172px;height:29px;background:linear-gradient(90deg,#d8d8d4,#f1efe9 50%,#e3e6dd);color:#222"><span>Rein vegetarische<br>Spezialitäten, tafelfertig</span></div>
  <table class="pl" style="left:230px;top:46px;width:172px">
    <tr><th></th><th>Nr.</th><th>Gebinde</th><th>Inhalt</th><th>Euro</th><th>Karton</th><th>EAN</th><th>Preis</th></tr>
    <tr><td class="n">Broccoli-Creme-Suppe</td><td>077</td><td>1/4 Dose</td><td>212 ml</td><td>1,40</td><td>50x1</td><td>001718</td><td>70,00</td></tr>
    <tr><td class="n">Möhren-Ingwer-Suppe</td><td>119</td><td>1/4 Dose</td><td>212 ml</td><td>1,40</td><td>50x1</td><td>002492</td><td>70,00</td></tr>
    <tr><td class="n">Kürbis-Mango-Suppe</td><td>120</td><td>1/4 Dose</td><td>212 ml</td><td>1,40</td><td>50x1</td><td>006354</td><td>70,00</td></tr>
    <tr><td class="n">Fruchtige Tomatensuppe</td><td>070</td><td>1/4 Dose</td><td>212 ml</td><td>1,40</td><td>50x1</td><td>001859</td><td>70,00</td></tr>
    <tr><td class="n">Klare Zwiebelsuppe</td><td>074</td><td>1/4 Dose</td><td>212 ml</td><td>1,40</td><td>50x1</td><td>000790</td><td>70,00</td></tr>
    <tr><td class="n">Champignon-Creme-Suppe</td><td>115</td><td>1/4 Dose</td><td>212 ml</td><td>1,40</td><td>50x1</td><td>001840</td><td>70,00</td></tr>
    <tr><td class="n">Tomaten-Creme</td><td>116</td><td>1/4 Dose</td><td>212 ml</td><td>1,40</td><td>50x1</td><td>001830</td><td>70,00</td></tr>
    <tr><td class="n">Spargel-Creme-Suppe</td><td>119</td><td>1/4 Dose</td><td>212 ml</td><td>1,40</td><td>50x1</td><td>006730</td><td>70,00</td></tr>
  </table>
  <div class="banner" role="img" aria-label="Foto einer roten Tomatensuppe mit Kräutern" style="left:230px;top:113px;width:172px;height:30px;background:linear-gradient(90deg,#b51d12,#d93a22 50%,#c2261a)"><span>Ringpull-Dosen für<br>1 Suppentasse</span></div>
  <div class="sub" style="left:230px;top:145px">Auch in 24/4 Kartons</div>
  <table class="pl" style="left:230px;top:152px;width:172px">
    <tr><th></th><th>Nr.</th><th>Gebinde</th><th>Inhalt</th><th>Euro</th><th>Karton</th><th>EAN</th><th>Preis</th></tr>
    <tr><td class="n">Kartoffel-Suppen-Terrine</td><td>062</td><td>1/4 Dose</td><td>212 ml</td><td>1,40</td><td>50x1</td><td>000301</td><td>70,00</td></tr>
    <tr><td class="n">Hühnersuppe klar</td><td>137</td><td>1/4 Dose</td><td>212 ml</td><td>1,40</td><td>50x1</td><td>001380</td><td>70,00</td></tr>
    <tr><td class="n">Rindsuppe mit Einlage</td><td>107</td><td>1/4 Dose</td><td>212 ml</td><td>1,40</td><td>50x1</td><td>001418</td><td>70,00</td></tr>
    <tr><td class="n">Hühnersuppe mit Prinzessnudeln</td><td>104</td><td>1/4 Dose</td><td>212 ml</td><td>1,40</td><td>50x1</td><td>001519</td><td>70,00</td></tr>
    <tr><td class="n">Hühnersuppe mit Eierstich + Reis</td><td>106</td><td>1/4 Dose</td><td>212 ml</td><td>1,40</td><td>50x1</td><td>001618</td><td>70,00</td></tr>
    <tr><td class="n">Tomatensuppe mit Fleischklößchen</td><td>065</td><td>1/4 Dose</td><td>212 ml</td><td>1,40</td><td>50x1</td><td>000924</td><td>70,00</td></tr>
    <tr><td class="n">Serbische Bohnensuppe</td><td>052</td><td>1/4 Dose</td><td>212 ml</td><td>1,40</td><td>50x1</td><td>000524</td><td>70,00</td></tr>
    <tr><td class="n">Gebundene Ochsenschwanzsuppe</td><td>138</td><td>1/4 Dose</td><td>212 ml</td><td>1,40</td><td>50x1</td><td>002387</td><td>70,00</td></tr>
    <tr><td class="n">Gulaschsuppe mit Einlage</td><td>129</td><td>1/4 Dose</td><td>212 ml</td><td>1,40</td><td>50x1</td><td>003384</td><td>70,00</td></tr>
    <tr><td class="n">Kessel-Gulasch-Suppe</td><td>097</td><td>1/4 Dose</td><td>212 ml</td><td>1,40</td><td>50x1</td><td>004750</td><td>70,00</td></tr>
    <tr><td class="n">Grüne Pfeffersuppe</td><td>092</td><td>1/4 Dose</td><td>212 ml</td><td>1,40</td><td>50x1</td><td>001924</td><td>70,00</td></tr>
    <tr><td class="n">Markklößchensuppe</td><td>201</td><td>1/4 Dose</td><td>212 ml</td><td>1,40</td><td>50x1</td><td>002160</td><td>70,00</td></tr>
    <tr><td class="n">Linsensuppe nach Landhausart</td><td>059</td><td>1/4 Dose</td><td>212 ml</td><td>1,40</td><td>50x1</td><td>005590</td><td>70,00</td></tr>
    <tr><td class="n">Minestrone italienisch</td><td>133</td><td>1/4 Dose</td><td>212 ml</td><td>1,40</td><td>50x1</td><td>005609</td><td>70,00</td></tr>
    <tr><td class="n">Leberknödel-Suppe</td><td>208</td><td>1/4 Dose</td><td>212 ml</td><td>1,40</td><td>50x1</td><td>005807</td><td>70,00</td></tr>
  </table>
</section>

<!-- Doppelseite 3 -->
<section class="page" style="left:39px;top:399px;width:422px;height:299px">
  <div class="brand" style="left:67px;top:16px">Morvak<small>Foodservice</small></div>
  <div class="banner" role="img" aria-label="Foto einer Tomatensuppe mit Kräutern" style="left:21px;top:46px;width:173px;height:30px;background:linear-gradient(90deg,#a91b10,#d63a24 50%,#bf2716)"><span>Pour Gourmets</span></div>
  <div class="sub" style="left:21px;top:78px">Tafelfertig für 2 Suppentassen</div>
  <table class="pl" style="left:21px;top:85px;width:173px">
    <tr><th></th><th>Nr.</th><th>Gebinde</th><th>Inhalt</th><th>Euro</th><th>Karton</th><th>EAN</th><th>Preis</th></tr>
    <tr><td class="n">Kessel-Gulasch<small>mit reichlicher Einlage</small></td><td>164</td><td>1/2 Dose</td><td>425 ml</td><td>1,95</td><td>12x1</td><td>00865</td><td>23,40</td></tr>
    <tr><td class="n">Klare Zwiebelsuppe<small>nach Bistro-Art, mit Weißwein</small></td><td>075</td><td>1/2 Dose</td><td>425 ml</td><td>1,95</td><td>12x1</td><td>00864</td><td>23,40</td></tr>
    <tr><td class="n">Hühnersuppe<small>mit Eierstich und Reis, Gemüse</small></td><td>087</td><td>1/2 Dose</td><td>425 ml</td><td>1,95</td><td>12x1</td><td>00437</td><td>23,40</td></tr>
    <tr><td class="n">Fruchtige Tomatencreme<small>Provence mit Tomatenwürfeln</small></td><td>071</td><td>1/2 Dose</td><td>425 ml</td><td>1,95</td><td>12x1</td><td>00659</td><td>23,40</td></tr>
  </table>
  <div class="banner" role="img" aria-label="Foto einer gelben Brühe mit Kräutern" style="left:21px;top:146px;width:173px;height:30px;background:linear-gradient(90deg,#e3c06a,#d6a02a 50%,#c88718)"><span>Die feine Basis für<br>Suppen und Saucen</span></div>
  <table class="pl" style="left:21px;top:180px;width:173px">
    <tr><th></th><th>Nr.</th><th>Gebinde</th><th>Euro</th><th>Ergiebig.</th><th>Karton</th><th>EAN</th><th>Preis</th></tr>
    <tr><td class="n">Rindbouillon<small>kräftig – zum Kochen und Würzen</small></td><td>149</td><td>1 kg Ringpull</td><td>10,95</td><td>für 50 Liter</td><td>6x1</td><td>002305</td><td>65,70</td></tr>
    <tr><td class="n">Hühnerbouillon doppelt<small>aus besten Zutaten – 40g je Liter</small></td><td>144</td><td>1 kg Ringpull</td><td>12,35</td><td>für 25 Liter</td><td>6x1</td><td>002038</td><td>74,10</td></tr>
  </table>
  <div class="abs" style="left:21px;top:216px;width:173px;text-align:center;font-size:3.4px;font-weight:700">Alle Morvak-Produkte haben eine garantierte Restlaufzeit von mindestens 30 Monaten</div>
  <p class="copy" style="left:21px;top:226px;width:84px;font-size:2.4px;text-align:left"><b>Lieferungs- und Zahlungsbedingungen</b><br>Die Preise verstehen sich frei Haus, ohne Mwst. Die Ware bleibt bis zur vollständigen Bezahlung unser Eigentum. Sie kann nur im ordnungsgemäßen Geschäftsverkehr weiter veräußert werden. Der Käufer tritt jedoch die Forderung ab.</p>
  <p class="copy" style="left:110px;top:226px;width:84px;font-size:2.4px;text-align:left">die Vorbehaltsware ergeben, in jedem Falle an uns ab. Eine Sicherungsübereignung der Vorbehaltsware ist ausgeschlossen. Zahlung 30 Tage nach Rechnungsdatum netto Kasse. Erfüllungsort und Gerichtsstand ist der Sitz der Firma Morvak GmbH &amp; Co.</p>

  <div class="banner" role="img" aria-label="Foto klassischer Suppeneinlagen mit Klößchen und Petersilie" style="left:230px;top:14px;width:176px;height:32px;background:linear-gradient(90deg,#b9b048,#d8cc7a 50%,#c7b45a)"><span>Klassische Einlagen</span></div>
  <div class="sub" style="left:230px;top:48px">Die ideale Ergänzung jeder Suppe</div>
  <table class="pl" style="left:230px;top:56px;width:176px">
    <tr><th></th><th>Nr.</th><th>Gebinde</th><th>Inhalt</th><th>Euro</th><th>Karton</th><th>EAN</th><th>Preis</th></tr>
    <tr><td class="n">Eierstich<small>gewürfelt, nach Küchenmeister Art</small></td><td>241</td><td>1/1 Dose</td><td>500g gewürfelt</td><td>6,45</td><td>12x1</td><td>00207</td><td>77,40</td></tr>
    <tr><td class="n">Markklößchen<small>besonders im Aussehen – delikat</small></td><td>243</td><td>1/1 Dose</td><td>100 Klößchen</td><td>7,50</td><td>12x1</td><td>00153</td><td>90,00</td></tr>
  </table>
  <div class="banner" role="img" aria-label="Foto frischer grüner Gemüse und Kräuter" style="left:230px;top:93px;width:176px;height:32px;background:linear-gradient(90deg,#3f7a1c,#6aa22f 50%,#4b8a22)"><span>Spezialitäten aus dem<br>Gemüsegarten</span></div>
  <table class="pl" style="left:230px;top:129px;width:176px">
    <tr><th></th><th>Nr.</th><th>Gebinde</th><th>Inhalt</th><th>Euro</th><th>Karton</th><th>EAN</th><th>Preis</th></tr>
    <tr><td class="n">Erbsensuppe – deftig</td><td>060</td><td>1/1 Dose</td><td>850 ml</td><td>2,55</td><td>12x1</td><td>00420</td><td>30,60</td></tr>
    <tr><td class="n">Kartoffelsuppe – rustikal</td><td>061</td><td>1/1 Dose</td><td>850 ml</td><td>2,55</td><td>12x1</td><td>00796</td><td>30,60</td></tr>
    <tr><td class="n">Linsensuppe – Terrine</td><td>063</td><td>1/1 Dose</td><td>850 ml</td><td>2,55</td><td>12x1</td><td>006309</td><td>30,60</td></tr>
  </table>
  <div class="banner" role="img" aria-label="Foto eines Fleischgerichts in heller Sauce" style="left:230px;top:166px;width:176px;height:32px;background:linear-gradient(90deg,#d98a3a,#efd8b8 50%,#e6c39a);color:#222"><span>Fleischkonserven</span></div>
  <div class="sub" style="left:230px;top:200px">In hervorragender Qualität</div>
  <table class="pl" style="left:230px;top:207px;width:176px">
    <tr><th></th><th>Nr.</th><th>Gebinde</th><th>Inhalt</th><th>Euro</th><th>Karton</th><th>EAN</th><th>Preis</th></tr>
    <tr><td class="n">Labskaus hausgemacht<small>nach Hafenrezept</small></td><td>212</td><td>1/1 Dose</td><td>850 ml</td><td>4,45</td><td>12x1</td><td>00104</td><td>53,40</td></tr>
    <tr><td class="n">Ragout fin aus Kalb<small>und Geflügel, feinste Art</small></td><td>122</td><td>1/4 Ringpull</td><td>1 große Portion</td><td>3,25</td><td>50x1</td><td>00102</td><td>162,50</td></tr>
    <tr><td class="n">Ragout fin<small>ohne Brät und ohne Farce</small></td><td>126</td><td>1/1 Dose</td><td>4 große Portionen</td><td>10,00</td><td>12x1</td><td>00100</td><td>120,00</td></tr>
  </table>
</section>

<!-- Rückseite -->
<section class="page" style="left:494px;top:400px;width:212px;height:300px">
  <div class="photo" role="img" aria-label="Foto einer orangefarbenen Kürbissuppe mit Sahne und Kürbiskernen in weißer Schale" style="inset:0;background:radial-gradient(ellipse at 78% 62%,#e88a10 0%,#f3a726 28%,#f6cf7e 48%,#fbf6ee 68%,#f4f1ec 100%)"></div>
  <div class="brand" style="left:66px;top:16px">Morvak<small>Foodservice</small></div>
  <div class="abs" style="left:0;width:212px;top:272px;text-align:center;font-size:3.2px;line-height:1.4;color:#444">
    <b>MORVAK GMBH &amp; CO. KG</b><br>
    Lindenallee 12 · 40210 Altheim · 02151 · 4038821 · Fax 40388 und 40389<br>
    info@morvak-eintopf.de · www.morvak-eintopf.de
  </div>
</section>

</body>
</html>
```